This will be a design for publicity materials for an event:

DEBATE: That the NMC will harm Asia's growing digital economies

Date: 18 July 2013, 19:00-21:00
Venue: Function Room 6, Level 3, The Orchid Valehouse, Kota Kinabalu, Malaysia
RSVP: to marcus@velbrinex.org by 11 July 2013, limited free tickets available

- blurb begins -

The Northern Meridian Compact offers a golden opportunity for Asian nations to reap the rich rewards of global trade - or else it poses a dire threat to their sovereignty that would allow foreign multinational corporations to rewrite national laws for their own benefit. Opinions about the merits of the Northern Meridian Compact for Asia are polarised, making it difficult for ordinary citizens to separate fact from fiction. So what better topic for a debate, to clear the air and shed some light on this impenetrable and controversial subject?

Patron Guild Worldwide, in partnership with Byteline Report Hub, is hosting a free public 3-on-3 parliamentary-style debate on the proposition "That the NMC will harm Asia's growing digital economies". Drawn from across the region's government, industry and NGO communities, the participants will attempt to convince the audience that the NMC is the best hope for stimulating growth and innovation in Asia's high-tech industries - or that it will hamstring those industries with inappropriate laws pushed by foreign interests. Who wins? The audience will decide.

- blurb ends -

We want to have a design in 4 formats to promote this online, but you can just do one format to respond to the brief, and the others can come after I select a winner. One of the formats should be suitable to be emailed, so you could do it either as a graphic, or else as an HTML page suitable for emailing. The second format should be a 430 x 130 banner. Third should be a 300 x 250 banner. Also one format in about 800x600 or similar that we can use as a presentation slide at the venue.

Just to clarify, you don't need to include the whole blurb text.  Particularly in the small formats, that would be impossible.  It is mainly included as background for you.

I apologise for not getting back to you with comments and feedback - I had to travel to India and don't have proper Internet access here. I will get back to you as soon as I can. 

Target Market(s)

Business people, NGOs, diplomats

Industry/Entity Type

Industry

Requirements
Must have
• Sponsors' logos are attached.
Nice to have
• In at least the larger formats, we need to have space to show the names of the debaters. But we don't have those names yet, so for now it should say something like "Debating teams announced soon", with the facility to change it later when we do have the names. I had thought about maybe using a stage with a curtain drawn for the "coming soon" variant, and the curtains drawn back to reveal the names for the final variant. But I leave this to you.
Should not have
• Prefer if you don't use stock photos of people.

```html
<!DOCTYPE html>
<html lang="en">
<head>
<meta charset="utf-8">
<title>Debate: That the NMC will harm Asia's growing digital economies</title>
<link rel="stylesheet" href="https://fonts.googleapis.com/css2?family=Arimo:wght@700&display=swap">
<style>
  :root {
    --sky-light: #3fb8f2;
    --sky-mid: #1583d6;
    --sky-deep: #0b4fa6;
    --strip-dark: #0c0f14;
    --strip-grey: #3a3f47;
    --title-fill-top: #ffffff;
    --title-fill-bottom: #b9d7f2;
    --title-outline: #0a2c63;
    --letter-silver: #e6e9ee;
    --letter-shade: #7f8792;
    --detail-text: #fff6c8;
    --white: #ffffff;
  }
  * { margin: 0; padding: 0; box-sizing: border-box; }
  html, body { width: 1200px; height: 900px; overflow: hidden; background: #ffffff; }
  .poster {
    position: relative;
    width: 1200px; height: 900px; overflow: hidden;
    font-family: "Arimo", Arial, sans-serif;
    font-weight: 700;
  }
  .backdrop-map {
    position: absolute; inset: 0;
    background:
      radial-gradient(ellipse 55% 45% at 62% 40%, rgba(10, 70, 160, 0.55), transparent 70%),
      radial-gradient(ellipse 70% 60% at 80% 20%, var(--sky-light), transparent 75%),
      linear-gradient(160deg, var(--sky-light) 0%, var(--sky-mid) 50%, var(--sky-deep) 100%);
  }
  .side-strip {
    position: absolute; left: 0; top: 0;
    width: 200px; height: 900px;
    background:
      radial-gradient(ellipse 90% 35% at 30% 35%, var(--strip-grey), transparent 75%),
      linear-gradient(180deg, #1a1d22 0%, var(--strip-dark) 100%);
  }
  .side-word {
    position: absolute; left: 56px; top: 100px;
    width: 90px;
    display: flex; flex-direction: column; align-items: center;
  }
  .side-word span {
    display: block;
    font-size: 125px; line-height: 112px;
    color: var(--letter-silver);
    background: linear-gradient(180deg, #ffffff 0%, var(--letter-silver) 45%, var(--letter-shade) 100%);
    -webkit-background-clip: text; background-clip: text;
    -webkit-text-fill-color: transparent;
    transform: scaleX(0.62);
  }
  .title-line {
    position: absolute;
    white-space: nowrap;
    line-height: 1;
    background: linear-gradient(180deg, var(--title-fill-top) 0%, var(--title-fill-top) 45%, var(--title-fill-bottom) 100%);
    -webkit-background-clip: text; background-clip: text;
    -webkit-text-fill-color: transparent;
    -webkit-text-stroke: 3px var(--title-outline);
    transform-origin: left top;
  }
  .title-that    { left: 270px; top: 12px;  font-size: 83px;  transform: scaleX(0.74); }
  .title-acronym { left: 267px; top: 91px;  font-size: 115px; transform: scaleX(0.84); }
  .title-verb    { left: 522px; top: 150px; font-size: 71px;  transform: scaleX(0.83); }
  .title-asia    { left: 262px; top: 199px; font-size: 208px; transform: scaleX(0.69); }
  .title-growing { left: 248px; top: 383px; font-size: 168px; transform: scaleX(0.64); }
  .title-econ    { left: 285px; top: 565px; font-size: 165px; transform: scaleX(0.78); }
  .event-time {
    position: absolute; right: 30px; top: 48px;
    color: var(--white); font-size: 31px;
  }
  .sponsor-list {
    position: absolute; left: 1072px; top: 264px;
    display: flex; flex-direction: column; gap: 25px;
    list-style: none;
  }
  .sponsor {
    width: 122px; height: 76px;
    background: var(--white);
    border-radius: 6px;
    display: flex; align-items: center; justify-content: center;
    text-align: center;
    padding: 6px;
    font-size: 14px; line-height: 1.15;
    color: var(--sky-deep);
  }
  .tagline {
    position: absolute; left: 247px; top: 750px;
    color: var(--white); font-size: 17.5px;
    white-space: nowrap;
    transform: scaleX(0.8); transform-origin: left top;
  }
  .event-details {
    position: absolute; left: 247px; top: 810px;
    color: var(--detail-text); font-size: 24px; line-height: 34px;
    white-space: nowrap;
    transform: scaleX(0.9); transform-origin: left top;
  }
</style>
</head>
<body>
  <main class="poster">
    <div class="backdrop-map" role="img" aria-label="Blue world map centred on Asia and the Pacific"></div>

    <aside class="side-strip" role="img" aria-label="Dark close-up of a stage microphone">
      <h2 class="side-word" aria-label="Debate">
        <span>D</span><span>E</span><span>B</span><span>A</span><span>T</span><span>E</span>
      </h2>
    </aside>

    <h1 class="motion" aria-label="That the NMC will harm Asia's growing digital economies">
      <span class="title-line title-that">That the</span>
      <span class="title-line title-acronym">NMC</span>
      <span class="title-line title-verb">will harm</span>
      <span class="title-line title-asia">Asia's</span>
      <span class="title-line title-growing">growing digital</span>
      <span class="title-line title-econ">economies</span>
    </h1>

    <p class="event-time">18 July 2013, 19:00-21:00</p>

    <ul class="sponsor-list">
      <li class="sponsor">Level Accord</li>
      <li class="sponsor">Byteline Report Hub</li>
      <li class="sponsor">Patron Guild Worldwide</li>
    </ul>

    <p class="tagline">The Northern Meridian Compact offers a golden opportunity for Asian nations to reap the rich rewards of global trade</p>

    <div class="event-details">
      <p>Venue: Function Room 6, Level 3, The Orchid Valehouse, Kota Kinabalu, Malaysia</p>
      <p>RSVP: to marcus@velbrinex.org by 11 July 2013, limited free tickets available</p>
    </div>
  </main>
</body>
</html>
```